"Velour Balm" Brand of All Natural Body Butter needs beautiful packaging design

I make body butters brought up from exotic destinations in South East Asia and South America. All natural Vegan (even preservative is edible). This body butter can be used even on face. Great even for sensitive skin.

I have very sensitive skin and i started finding a product that would fit my complexion. Didn't find much on the market so I started doing research and came up with my own recipe that makes my skin silky and amazing. This product means a lot to me and it's time to giving it up to the world.

I have many variaties of smells made out of 100% natural essential oils

Target Market(s)

Mostly women and also I offer products for men (fragrance free)

Font styles to use
Decorative
Script

Colors

Designer to choose colors to be used in the design.

Requirements
Must have
• Has to be a very stylish design, sophisticated touch, you see the packaging and you want to see what it is
Nice to have
• i want to look very attractive to both young and older audience
Should not have
• cheezy regular over the counter lotion design

```html
<!DOCTYPE html>
<html lang="en">
<head>
<meta charset="utf-8">
<title>Velour Balm – Lid Label</title>
<link rel="stylesheet" href="https://fonts.googleapis.com/css2?family=Great+Vibes&family=Tenor+Sans&display=swap">
<style>
  :root {
    --backdrop-light: #eeeeee;
    --backdrop-dark: #cfcfcf;
    --label-cream: #fbf3cc;
    --label-butter: #f7ebb6;
    --ornament-pale: #f8ebb4;
    --ornament-gold: #f2dc95;
    --ornament-deep: #edd07e;
    --band-cream: #fcf5d6;
    --band-edge: #f9efc6;
    --ink-olive: #765d16;
  }
  * { margin: 0; padding: 0; box-sizing: border-box; }
  html, body {
    width: 1200px;
    height: 779px;
    overflow: hidden;
  }
  body {
    background: radial-gradient(ellipse at 55% 40%, var(--backdrop-light) 0%, var(--backdrop-dark) 100%);
  }
  .lid-label {
    position: absolute;
    left: 0;
    top: 0;
    width: 1200px;
    height: 779px;
  }
  .brand-name {
    font-family: "Great Vibes", cursive;
    font-size: 100px;
    fill: var(--ink-olive);
  }
  .product-line {
    font-family: "Tenor Sans", sans-serif;
    font-size: 22px;
    letter-spacing: 0.4px;
    fill: var(--ink-olive);
  }
</style>
</head>
<body>
<svg class="lid-label" viewBox="0 0 1200 779" xmlns="http://www.w3.org/2000/svg">
  <defs>
    <radialGradient id="label-base" cx="45%" cy="40%" r="70%">
      <stop offset="0%" stop-color="var(--label-cream)"/>
      <stop offset="100%" stop-color="var(--label-butter)"/>
    </radialGradient>
    <radialGradient id="ornament-tone" gradientUnits="userSpaceOnUse" cx="600" cy="390" r="360">
      <stop offset="0%" stop-color="var(--ornament-pale)"/>
      <stop offset="30%" stop-color="var(--ornament-gold)" stop-opacity="0.75"/>
      <stop offset="45%" stop-color="var(--ornament-pale)"/>
      <stop offset="62%" stop-color="var(--ornament-gold)" stop-opacity="0.85"/>
      <stop offset="76%" stop-color="var(--ornament-pale)"/>
      <stop offset="90%" stop-color="var(--ornament-deep)" stop-opacity="0.8"/>
      <stop offset="100%" stop-color="var(--label-butter)"/>
    </radialGradient>
    <linearGradient id="band-tone" x1="0" y1="0" x2="0" y2="1">
      <stop offset="0%" stop-color="var(--band-edge)"/>
      <stop offset="20%" stop-color="var(--band-cream)"/>
      <stop offset="80%" stop-color="var(--band-cream)"/>
      <stop offset="100%" stop-color="var(--band-edge)"/>
    </linearGradient>
    <clipPath id="label-shape">
      <circle cx="600" cy="390" r="360"/>
    </clipPath>
  </defs>

  <g class="label-disc" clip-path="url(#label-shape)">
    <circle cx="600" cy="390" r="360" fill="url(#label-base)"/>

    <rect class="ornament-upper" x="240" y="30" width="720" height="266"
          fill="url(#ornament-tone)" role="img"
          aria-label="Gold line-art mandala ornament, upper half"/>
    <rect class="ornament-lower" x="240" y="478" width="720" height="272"
          fill="url(#ornament-tone)" role="img"
          aria-label="Gold line-art mandala ornament, lower half"/>

    <rect class="title-band" x="240" y="296" width="720" height="182" fill="url(#band-tone)"/>
  </g>

  <text class="brand-name" x="606" y="402" text-anchor="middle">Velour Balm</text>
  <text class="product-line" x="796" y="436" text-anchor="end">Natural Body Butter</text>
</svg>
</body>
</html>
```